" A empresa está localizada numa cidade pequena, porém muito próximos da capital do estado de Minas Gerais e de outras cidades maiores do interior. Considerada região metropolitana da capital. Criaremos um site e faremos venda de produtos na loja virtual, bem como marcação de serviços. Queremos trazer profissionalismo e um serviço diferenciado para a região. Nossa meta é em 3 anos ser a principal referência nesse serviço num raio de 50 km da cidade. "

```html
<!DOCTYPE html>
<html lang="pt-BR">
<head>
<meta charset="utf-8">
<title>Cartão de visita — Folha Clara</title>
<link href="https://fonts.googleapis.com/css2?family=Nunito:wght@400;600&display=swap" rel="stylesheet">
<style>
  :root {
    --bg: #e9e9e9;
    --teal: #7fada8;
    --teal-dark: #5f8f8a;
    --brand: #3f3324;
    --paper: #ffffff;
    --ink: #6b6b6b;
  }
  * { margin: 0; padding: 0; box-sizing: border-box; }
  html, body { width: 1200px; height: 1200px; overflow: hidden; }
  body { background: var(--bg); position: relative; font-family: "Nunito", sans-serif; }

  .card {
    position: absolute; left: 170px; width: 860px; height: 470px;
    border-radius: 26px; overflow: hidden;
    box-shadow: 0 10px 24px rgba(0,0,0,.12);
  }
  .card-front { top: 110px; background: var(--teal); display: flex; align-items: center; justify-content: center; }
  .card-back { top: 620px; background: var(--paper); }

  .brand { display: flex; align-items: center; gap: 18px; }
  .brand-mark { flex: none; width: 56px; height: 56px; border-radius: 50%; background: var(--paper); opacity: .85; }
  .brand-name { font-family: "Nunito", sans-serif; font-weight: 600; color: var(--brand); font-size: 60px; line-height: 1; white-space: nowrap; }

  .back-panel {
    position: absolute; left: 0; top: 0; width: 360px; height: 285px;
    background: var(--teal); border-bottom-right-radius: 22px;
    display: flex; align-items: center; justify-content: center;
  }
  .back-panel .brand { gap: 12px; }
  .back-panel .brand-mark { width: 34px; height: 34px; }
  .back-panel .brand-name { font-size: 36px; }

  .person-name {
    position: absolute; left: 0; width: 360px; top: 340px;
    text-align: center; color: var(--teal-dark); font-size: 26px; font-weight: 600;
  }

  .contact-list { position: absolute; left: 398px; top: 40px; list-style: none; }
  .contact-item { display: flex; align-items: center; gap: 14px; color: var(--ink); font-size: 20px; line-height: 1.2; margin-bottom: 19px; }
  .contact-icon { flex: none; width: 30px; height: 30px; border-radius: 50%; background: var(--teal); display: flex; align-items: center; justify-content: center; }
  .contact-icon svg { width: 17px; height: 17px; }
</style>
</head>
<body>

<section class="card card-front">
  <div class="brand">
    <span class="brand-mark"></span>
    <span class="brand-name">FOLHA CLARA</span>
  </div>
</section>

<section class="card card-back">
  <div class="back-panel">
    <div class="brand">
      <span class="brand-mark"></span>
      <span class="brand-name">FOLHA CLARA</span>
    </div>
  </div>
  <div class="person-name">Helena Duarte</div>

  <ul class="contact-list">
    <li class="contact-item">
      <span class="contact-icon"><svg viewBox="0 0 24 24"><path fill="#fff" d="M6.6 10.8a15 15 0 0 0 6.6 6.6l2.2-2.2c.3-.3.7-.4 1-.2 1.1.4 2.3.6 3.6.6.6 0 1 .4 1 1V20c0 .6-.4 1-1 1A17 17 0 0 1 3 4c0-.6.4-1 1-1h3.5c.6 0 1 .4 1 1 0 1.3.2 2.5.6 3.6.1.3 0 .7-.2 1z"/></svg></span>
      (31) 9 9000-1234
    </li>
    <li class="contact-item">
      <span class="contact-icon"><svg viewBox="0 0 24 24"><rect x="3" y="6" width="18" height="12" rx="1.5" fill="none" stroke="#fff" stroke-width="2"/><path d="M3.5 7l8.5 6 8.5-6" fill="none" stroke="#fff" stroke-width="2"/></svg></span>
      helenaduarte@folhaclara.net
    </li>
    <li class="contact-item">
      <span class="contact-icon"><svg viewBox="0 0 24 24"><circle cx="12" cy="12" r="8.5" fill="none" stroke="#fff" stroke-width="2"/><ellipse cx="12" cy="12" rx="3.5" ry="8.5" fill="none" stroke="#fff" stroke-width="1.6"/><path d="M3.5 12h17" stroke="#fff" stroke-width="1.6"/></svg></span>
      www.folhaclara.net.br
    </li>
    <li class="contact-item">
      <span class="contact-icon"><svg viewBox="0 0 24 24"><path fill="#fff" d="M12 2a7 7 0 0 0-7 7c0 5 7 13 7 13s7-8 7-13a7 7 0 0 0-7-7zm0 9.5A2.5 2.5 0 1 1 12 6.5a2.5 2.5 0 0 1 0 5z"/></svg></span>
      <span>Rua das Acácias, 140<br>Vale Verde - MG</span>
    </li>
    <li class="contact-item">
      <span class="contact-icon"><svg viewBox="0 0 24 24"><path d="M10 14l4-4M9 7.5l1.5-1.5a3.5 3.5 0 0 1 5 5L14 12.5M10 11.5L8.5 13a3.5 3.5 0 0 0 5 5L15 16.5" fill="none" stroke="#fff" stroke-width="2" stroke-linecap="round"/></svg></span>
      folhaclara.net
    </li>
    <li class="contact-item">
      <span class="contact-icon"><svg viewBox="0 0 24 24"><path d="M4 5h16v11H9l-5 4z" fill="none" stroke="#fff" stroke-width="2" stroke-linejoin="round"/></svg></span>
      @folhaclara18
    </li>
  </ul>
</section>

</body>
</html>
```